Yoga class opening. Little schedule for JUNE JULY and AUGUST

Flyer to promote an opening yoga class. The color of the docx haven't to be respected.

We want something joyfull, professional, clean and serious.

About the logo we oppened a contest at the same time so at the moment there is no logo but the logo color will be simple.

The phone number will change so you can poste a random one for the design that i can change by myself.

i recieved many creation in both side BUT i want something in 1 side :)

Yoga student. all age

It Professional

Yoga brook

Sans Serif

• The text present on the docx
• Some symbols about yoga ( Namasté signs, mandala, ... )
• Not too much details it has to be clear.

```html
<!DOCTYPE html>
<html lang="fr">
<head>
<meta charset="utf-8">
<title>Yoga Brook – Stages et ateliers d'été</title>
<link href="https://fonts.googleapis.com/css2?family=Roboto+Condensed:wght@400;700&display=swap" rel="stylesheet">
<style>
  :root {
    --stage: #1d6a92;
    --pink: #e56aa6;
    --band: #f4c6dd;
    --footer: #c9507f;
    --deep: #8c1d58;
    --ink: #3a0d24;
    --white: #ffffff;
    --logo-pink: #e0308a;
    --stripe-1: #f0a27d;
    --stripe-2: #e9787f;
    --stripe-3: #e24a93;
    --stripe-4: #c8307a;
  }
  * { margin: 0; padding: 0; box-sizing: border-box; }
  html, body { width: 1200px; height: 1200px; overflow: hidden; }
  body {
    background: var(--stage);
    font-family: "Roboto Condensed", sans-serif;
    position: relative;
  }
  .flyer {
    position: absolute;
    left: 136px; top: 0;
    width: 927px; height: 1200px;
    background: radial-gradient(ellipse at 50% 25%, #f6b3d6 0%, var(--pink) 45%, #e15f9f 100%);
    overflow: hidden;
    color: var(--white);
  }
  .stripes { position: absolute; top: 102px; height: 100px; }
  .stripes span { display: block; }
  .stripes span:nth-child(1) { height: 28px; background: var(--stripe-1); }
  .stripes span:nth-child(2) { height: 32px; background: var(--stripe-2); }
  .stripes span:nth-child(3) { height: 26px; background: var(--stripe-3); }
  .stripes span:nth-child(4) { height: 14px; background: var(--stripe-4); }
  .stripes-left { left: 0; width: 190px; }
  .stripes-right {
    right: 0; width: 260px;
    -webkit-mask-image: linear-gradient(90deg, transparent 0%, #000 35%);
    mask-image: linear-gradient(90deg, transparent 0%, #000 35%);
  }

  .logo {
    position: absolute; left: 61px; top: 35px;
    width: 244px; height: 244px; border-radius: 50%;
    background: var(--white);
    display: flex; align-items: center; justify-content: center;
  }
  .logo-name {
    font-weight: 700; font-size: 36px; color: var(--logo-pink);
    white-space: nowrap;
  }
  .call {
    position: absolute; right: 42px; top: 112px;
    text-align: right; font-size: 33px; line-height: 36px;
  }
  .hero-art {
    position: absolute; left: 276px; top: 30px;
    width: 400px; height: 320px;
    border-radius: 50%;
    background: radial-gradient(circle, rgba(255,235,245,.95) 0%, rgba(248,190,222,.7) 45%, rgba(229,106,166,0) 72%);
  }
  .intro {
    position: absolute; left: 0; width: 100%; top: 342px;
    text-align: center; color: var(--deep);
    font-size: 23px; line-height: 30px; padding-left: 10px;
  }
  .tagline {
    position: absolute; left: 0; width: 100%; top: 473px;
    text-align: center; font-size: 29px; line-height: 35px;
  }

  .month-band {
    position: absolute; left: 0; right: 0; height: 34px;
    background: linear-gradient(90deg, rgba(244,198,221,0) 0%, var(--band) 14%, var(--band) 100%);
  }
  .month-title { position: absolute; font-size: 33px; line-height: 34px; }
  .col { position: absolute; font-size: 14.5px; color: var(--ink); }
  .col h3 {
    font-weight: 700; font-size: 17px; color: var(--white);
    margin-bottom: 16px; line-height: 18px; white-space: nowrap;
  }
  .col p { line-height: 24.4px; white-space: nowrap; }
  .col b { font-weight: 700; }
  .divider {
    position: absolute; left: 472px; width: 1px;
    background: rgba(255,255,255,.7);
  }

  .footer {
    position: absolute; left: 0; right: 0; top: 1077px; bottom: 0;
    background: var(--footer);
    border-top: 3px solid var(--band);
    text-align: center;
  }
  .footer .lead { font-size: 30px; margin-top: 6px; line-height: 36px; }
  .footer .info { font-size: 19px; line-height: 27px; }
</style>
</head>
<body>
<main class="flyer">
  <div class="stripes stripes-left"><span></span><span></span><span></span><span></span></div>
  <div class="stripes stripes-right"><span></span><span></span><span></span><span></span></div>

  <div class="hero-art" role="img" aria-label="Silhouette d'une personne en posture du lotus devant un mandala en fleur de lotus"></div>

  <div class="logo"><span class="logo-name">YOGA BROOK</span></div>

  <div class="call">CALL US NOW<br>987 654 321</div>

  <div class="intro">
    NOUVEAU !! VOTRE STUDIO DE YOGA A VALMONT<br>
    OUVERTURE LE 6 JUIN 2016 AU<br>
    212 RUE DES TILLEULS<br>
    4270 VALMONT
  </div>
  <div class="tagline">
    En attendant le planning des cours de la rentrée,<br>
    YOGA BROOK vous propose ses stages et ateliers d'été.
  </div>

  <div class="month-band" style="top:555px"></div>
  <div class="month-title" style="left:59px;top:555px">JUIN</div>
  <div class="col" style="left:59px;top:600px">
    <h3 style="margin-left:26px">Stage découverte du YOGA 10h00 85 €</h3>
    <p><b>Du lundi 6 au vendredi 10 juin :</b> 10h00 à 12h00 ou 18h00 à 20h00</p>
    <p><b>Du lundi 13 au vendredi 17 juin :</b> 10h00 à 12h00 ou 18h00 à 20h00</p>
    <p><b>Du lundi 20 au vendredi 24 juin :</b> 10h00 à 12h00 ou 18h00 à 20h00</p>
    <p><b>Du lundi 27 au vendredi 1er juillet :</b> 10h00 à 12h00 ou 18h00 à 20h00</p>
  </div>
  <div class="divider" style="top:610px;height:120px"></div>
  <div class="col" style="left:481px;top:600px">
    <h3 style="margin-left:27px">Atelier gestion du stress yoga/sophrologie 2h00 28 €</h3>
    <p><b>Samedi 11 juin</b> 10h30 à 12h30</p>
    <p><b>Samedi 11 juin</b> 15h à 17h00</p>
    <p><b>Dimanche 12 juin</b> 10h30 à 12h30</p>
    <p><b>Dimanche 12 juin</b> 14h à 16h00</p>
  </div>

  <div class="month-band" style="top:741px"></div>
  <div class="month-title" style="left:62px;top:742px">JUILLET</div>
  <div class="col" style="left:59px;top:786px">
    <h3>Stage initiation à l'ASHTANGA 10h00 85 €</h3>
    <p><b>Du lundi 4 au vendredi 8 juillet :</b> 10h00 à 12h00 ou 18h00 à 20h00</p>
    <p><b>Du lundi 11 au vendredi 15 juillet :</b> 10h00 à 12h00 ou 18h00 à 20h00</p>
    <p><b>Du lundi 18 au vendredi 22 juillet :</b> 10h00 à 12h00 ou 18h00 à 20h00</p>
    <p><b>Du lundi 25 au vendredi 29 juillet :</b> 10h00 à 12h00 ou 18h00 à 20h00</p>
  </div>
  <div class="divider" style="top:796px;height:120px"></div>
  <div class="col" style="left:481px;top:786px">
    <h3>Atelier gestion du stress yoga/sophrologie 2h00 28 €</h3>
    <p><b>Samedi 9 juillet</b> 10h30 à 12h30</p>
    <p><b>Samedi 9 juillet</b> 15h00 à 17h00</p>
    <p><b>Dimanche 10 juillet</b> 10h30 à 12h30</p>
    <p><b>Dimanche 10 juillet</b> 14h00 à 16h00</p>
  </div>

  <div class="month-band" style="top:931px"></div>
  <div class="month-title" style="left:59px;top:932px">AOUT</div>
  <div class="col" style="left:59px;top:977px">
    <h3>Stage découverte du YOGA 10h00 85 €</h3>
    <p><b>Du lundi 1er au vendredi 5 août :</b> 10h00 à 12h00 ou 18h00 à 20h00</p>
    <p><b>Du lundi 8 au vendredi 12 août :</b> 10h00 à 12h00 ou 18h00 à 20h00</p>
  </div>
  <div class="col" style="left:487px;top:1011px">
    <p><b>Du lundi 15 au vendredi 19 août :</b> 10h00 à 12h00 ou 18h00 à 20h00</p>
    <p><b>Du lundi 22 au vendredi 26 août :</b> 10h00 à 12h00 ou 18h00 à 20h00</p>
  </div>

  <footer class="footer">
    <p class="lead">Démarrage du planning annuel le 5 septembre 2016</p>
    <p class="info">Plus d'info et inscription : Ou via notre page Circlo : yoga brook</p>
    <p class="info">UN BEL ETE A TOUS !</p>
  </footer>
</main>
</body>
</html>
```